New Software Development Firm Needs Business Cards!

We just completed a successful logo design project on MakerHive and need to develop a business card design using that shiny new logo. We want a clean, modern design that communicates professionalism and tech savvy without being cliche'.

The company is "Bramble Logic, LLC", but our dba is "Bramble" The business card address should reflect the full company name in the address. The logo just uses "Bramble".

Photoshop or Illustrator source files will be required, along with exact font name(s) and source(s) used.

The design will need to work well with our letterhead as well. I'm also launching a project right now for letterhead and envelopes as well. Please submit to both projects! We're excited to see the designs. Thanks...

Target Market(s)

Small to medium business professionals

Industry/Entity Type

Business

Requirements
Must have
• Need place for:
- Company name and address (5 lines)
- Phone: (1 number)
- Fax: (1 number)
- Employee's name
- Employee's position
- Employee's email address
- Company web site URL
Nice to have
• Probably want a white card, but we're open to options.

```html
<!DOCTYPE html>
<html lang="en">
<head>
<meta charset="utf-8">
<title>Bramble Logic — Business Card</title>
<link href="https://fonts.googleapis.com/css2?family=Exo+2:wght@400&family=Source+Sans+3:wght@400;600&display=swap" rel="stylesheet">
<style>
  :root {
    --ink: #070707;
    --paper: #ffffff;
    --accent: #ed1c24;
    --text-grey: #4d4d4d;
    --name-grey: #555555;
    --page: #ffffff;
  }
  * { margin: 0; padding: 0; box-sizing: border-box; }
  html, body {
    width: 1200px; height: 1000px; overflow: hidden;
    background: var(--page);
    font-family: "Source Sans 3", "Myriad Pro", Arial, sans-serif;
  }
  .canvas { position: relative; width: 1200px; height: 1000px; }

  .card {
    position: absolute; left: 233px; width: 735px;
    box-shadow: 3px 5px 8px rgba(0,0,0,0.35);
    overflow: hidden;
  }
  .card-shapes { position: absolute; inset: 0; width: 100%; height: 100%; }

  .card--front { top: 43px; height: 420px; background: var(--ink); }
  .card--back { top: 526px; height: 422px; background: var(--paper); }

  .wordmark {
    position: absolute;
    font-family: "Exo 2", "Eurostile", sans-serif;
    font-weight: 400;
    line-height: 1;
    letter-spacing: 1px;
    white-space: nowrap;
  }
  .card--front .wordmark {
    left: 0; right: 0; text-align: center;
    top: 231px; font-size: 104px; color: var(--paper);
  }
  .card--back .wordmark {
    left: 52px; top: 28px; font-size: 100px; color: var(--ink);
  }

  .front-url {
    position: absolute; left: 0; right: 0; top: 351px;
    text-align: center; color: var(--paper);
    font-size: 18px; letter-spacing: 1.4px; line-height: 24px;
  }

  .person { position: absolute; left: 54px; top: 234px; }
  .person__name { font-size: 23px; font-weight: 600; color: var(--name-grey); line-height: 28px; }
  .person__role { font-size: 19px; color: var(--accent); line-height: 24px; }

  .contact {
    position: absolute; left: 406px; top: 214px;
    font-size: 19px; line-height: 25px; color: var(--text-grey);
  }
  .contact__company { color: var(--accent); }
  .contact__list { list-style: none; margin-top: 5px; }
  .contact__list li { display: flex; align-items: center; gap: 7px; }
  .contact__icon { width: 20px; height: 16px; flex: none; }

  .back-url {
    position: absolute; left: 403px; top: 389px;
    color: var(--paper); font-size: 18px; letter-spacing: 0.3px; line-height: 28px;
  }
</style>
</head>
<body>
<main class="canvas">

  <section class="card card--front" aria-label="Card front">
    <svg class="card-shapes" viewBox="0 0 735 420" aria-hidden="true">
      <polygon points="619,0 735,0 735,121" fill="var(--accent)"/>
    </svg>
    <div class="wordmark">Bramble</div>
    <p class="front-url">www.bramblelogic.com</p>
  </section>

  <section class="card card--back" aria-label="Card back">
    <svg class="card-shapes" viewBox="0 0 735 422" aria-hidden="true">
      <polygon points="619,0 735,0 735,122" fill="var(--accent)"/>
      <polygon points="0,385 109,385 121,422 0,422" fill="var(--accent)"/>
      <polygon points="139,385 735,385 735,422 124,422" fill="var(--ink)"/>
    </svg>
    <div class="wordmark">Bramble</div>

    <div class="person">
      <p class="person__name">Reed Hollis</p>
      <p class="person__role">Co Founder</p>
    </div>

    <div class="contact">
      <p class="contact__company">Bramble Logic, LLC</p>
      <p>418 Larkmoor Avenue, Suite 305</p>
      <p>Fairbrook, California 94871, USA</p>
      <ul class="contact__list">
        <li>
          <svg class="contact__icon" viewBox="0 0 20 16" aria-label="Phone" role="img">
            <path d="M2 6 Q10 0 18 6 L16 8 L13 6 L13 4 Q10 3 7 4 L7 6 L4 8 Z" fill="var(--accent)"/>
            <rect x="4" y="8" width="12" height="7" rx="1" fill="var(--accent)"/>
            <circle cx="10" cy="11.5" r="2" fill="var(--paper)"/>
          </svg>
          <span>(555) 014-2730</span>
        </li>
        <li>
          <svg class="contact__icon" viewBox="0 0 20 16" aria-label="Fax" role="img">
            <rect x="5" y="0" width="10" height="5" fill="var(--accent)"/>
            <rect x="2" y="5" width="16" height="10" rx="1.5" fill="var(--accent)"/>
            <rect x="5" y="8" width="10" height="2" fill="var(--paper)"/>
            <rect x="5" y="11" width="10" height="1.5" fill="var(--paper)"/>
          </svg>
          <span>(555) 014-2738</span>
        </li>
        <li>
          <svg class="contact__icon" viewBox="0 0 20 16" aria-label="Email" role="img">
            <rect x="1" y="2" width="18" height="12" fill="var(--accent)"/>
            <polyline points="1,2 10,9 19,2" fill="none" stroke="var(--paper)" stroke-width="1.5"/>
          </svg>
          <span>reed@bramblelogic.com</span>
        </li>
      </ul>
    </div>

    <p class="back-url">www.bramblelogic.com</p>
  </section>

</main>
</body>
</html>
```